Lydfern Primary School

We need to improve on our designs for a local School, Lydfern Primary.
One file contains the correct information required on the sign.
Our Mock ups are suggestions.
The School Uniform is blue -
We had these comments from our Client.
I can't decide whether to change the blue and try green to represent our commitment to outdoors, or maybe a combination of colours from the school badge, For the main sign options , I like them both but wondered if there was a way of combining the two? Slightly bigger badge.

I've included the files for the smaller signs if you were happy to provide a service to include all. We are a sign business focusing on other projects and external support will help. Thanks - Dermot.

```html
<!DOCTYPE html>
<html lang="en">
<head>
<meta charset="utf-8">
<title>Lydfern Primary School – Sign Options</title>
<link href="https://fonts.googleapis.com/css2?family=Poppins:wght@600;700&display=swap" rel="stylesheet">
<style>
  :root {
    --backdrop: #666666;
    --school-blue: #3278be;
    --deep-blue: #2a64a3;
    --leaf-green: #9fcd47;
    --sun-yellow: #f7d540;
    --sun-orange: #f39a32;
    --white: #ffffff;
    --text-shadow: #1d4f86;
  }
  html, body {
    margin: 0;
    padding: 0;
    width: 1199px;
    height: 1200px;
    overflow: hidden;
    background: var(--backdrop);
  }
  .sign-sheet {
    display: block;
    width: 1199px;
    height: 1200px;
    font-family: 'Poppins', sans-serif;
  }
  .panel-blue { fill: var(--school-blue); }
  .panel-green { fill: var(--leaf-green); }
  .panel-white { fill: var(--white); }
  .band-rule { fill: var(--deep-blue); }
  .frame-line { fill: none; stroke: var(--white); stroke-width: 3; }
  .badge-ring { fill: var(--white); }
  .badge-disc { fill: var(--sun-orange); }
  .badge-name { fill: var(--white); font-weight: 700; font-size: 40px; }
  .greeting { fill: var(--sun-yellow); font-weight: 700; font-size: 46px; }
  .school-name { fill: var(--white); font-weight: 700; }
  .school-name.shadow { fill: var(--text-shadow); }
  .motto { fill: var(--white); font-weight: 600; font-size: 38px; }
  .motto.on-white { fill: var(--school-blue); font-weight: 700; font-size: 46px; }
  .phone-line { fill: var(--white); font-weight: 700; font-size: 74px; }
  .contact-line { fill: var(--white); font-weight: 700; font-size: 28px; }
  .council-name { fill: var(--white); font-weight: 700; font-size: 13px; }
</style>
</head>
<body>
<svg class="sign-sheet" viewBox="0 0 1500 1500" xmlns="http://www.w3.org/2000/svg">
  <defs>
    <clipPath id="welcome-sign-shape">
      <path d="M253,243 H600 C640,243 650,127 750,127 C850,127 860,243 900,243 H1245 Q1265,243 1265,263 V610 Q1265,630 1245,630 H253 Q233,630 233,610 V263 Q233,243 253,243 Z"/>
    </clipPath>
    <clipPath id="entrance-sign-shape">
      <path d="M253,880 H600 C640,880 650,763 750,763 C850,763 860,880 900,880 H1245 Q1265,880 1265,900 V1353 Q1265,1373 1245,1373 H253 Q233,1373 233,1353 V900 Q233,880 253,880 Z"/>
    </clipPath>
  </defs>

  <!-- Welcome sign -->
  <g class="welcome-sign">
    <g clip-path="url(#welcome-sign-shape)">
      <rect class="panel-blue" x="230" y="120" width="1040" height="400"/>
      <rect class="band-rule" x="230" y="516" width="1040" height="8"/>
      <rect class="panel-green" x="230" y="524" width="1040" height="110"/>
    </g>
    <path class="frame-line" d="M252,262 H594 C628,262 640,149 750,149 C860,149 872,262 906,262 H1246 V612 H252 Z"/>
    <g class="school-badge" role="img" aria-label="Lydfern Primary School badge">
      <circle class="badge-ring" cx="750" cy="263" r="104"/>
      <circle class="badge-disc" cx="750" cy="263" r="96"/>
      <text class="badge-name" x="750" y="277" text-anchor="middle">LPS</text>
    </g>
    <text class="greeting" x="522" y="330" text-anchor="middle">Welcome</text>
    <text class="greeting" x="972" y="330" text-anchor="middle">Croeso</text>
    <text class="school-name shadow" x="752" y="432" text-anchor="middle" font-size="80">Lydfern Primary School</text>
    <text class="school-name" x="749" y="429" text-anchor="middle" font-size="80">Lydfern Primary School</text>
    <text class="motto" x="749" y="497" text-anchor="middle">'Wings to Fly, Roots to Grow'</text>
    <g class="phone-icon">
      <circle cx="408" cy="564" r="17" fill="var(--white)"/>
      <path d="M400,555 q-3,10 8,20 q6,4 9,1 l-3,-5 q-3,2 -6,-2 q-4,-4 -2,-7 l-4,-4 z" fill="var(--leaf-green)"/>
    </g>
    <text class="phone-line" x="775" y="592" text-anchor="middle">Tel: 01632 960 418</text>
  </g>

  <!-- Entrance sign -->
  <g class="entrance-sign">
    <g clip-path="url(#entrance-sign-shape)">
      <rect class="panel-blue" x="230" y="760" width="1040" height="394"/>
      <rect class="band-rule" x="230" y="1152" width="1040" height="8"/>
      <rect class="panel-white" x="230" y="1160" width="1040" height="88"/>
      <rect class="panel-green" x="230" y="1248" width="1040" height="130"/>
    </g>
    <path class="frame-line" d="M252,1160 V898 H594 C628,898 640,785 750,785 C860,785 872,898 906,898 H1246 V1160"/>
    <path class="frame-line" d="M252,1248 V1355 H1246 V1248"/>
    <g class="school-badge" role="img" aria-label="Lydfern Primary School badge">
      <circle class="badge-ring" cx="750" cy="900" r="104"/>
      <circle class="badge-disc" cx="750" cy="900" r="96"/>
      <text class="badge-name" x="750" y="914" text-anchor="middle">LPS</text>
    </g>
    <text class="school-name" x="749" y="1057" text-anchor="middle" font-size="60">Lydfern Primary School</text>
    <text class="school-name" x="749" y="1127" text-anchor="middle" font-size="60">Ysgol Gynradd Lydfern</text>
    <text class="motto on-white" x="749" y="1222" text-anchor="middle">Wings to fly, Roots to Grow</text>
    <text class="contact-line" x="716" y="1301" text-anchor="middle">Headteacher/Pennaeth - Mrs J. Harlow</text>
    <text class="contact-line" x="716" y="1334" text-anchor="middle">Tel: 01632 960 418</text>
    <g class="council-mark">
      <text class="council-name" x="1149" y="1298" text-anchor="middle">WESTVALE</text>
      <text class="council-name" x="1149" y="1316" text-anchor="middle">COUNCIL</text>
    </g>
  </g>
</svg>
</body>
</html>
```